Torvin Electrics Flyer Design Advertising

I am after an A5 Flyer design to help promote my electrical services business.
I would like to have information on what my business offers, photos of electrical work, and specials/deals for an amount of time.

Industry/Entity Type

Electrician

Font styles to use
Sans Serif

Colors
0292cd
33a6d7
85cae6
3176b5
333333
1b1b1b
ffffff
5c5c5c
474747

Requirements
Must have
• Specialising in New homes, renovations and commercial projects
• Contact details:
• ph. 0457 613 948
• email admin@torvinelectrics.com.au
• facebook TorvinElectrics
• Specials/Deals:
• 10% off all electrical services
• or
• Free LED downlights on installation
• *Terms conditions apply
• ALL RESIDENTIAL & COMMERCIAL ELECTRICAL SERVICES
• - New Home installations
• - Commercial projects
• - Shop fit outs
• - Renovations
• - Smoke Detectors
• - Air Conditioning and Ceiling Fans
• - Garden Lighting
• - Oven and Cooktop Installations
• - Power Point installation
• - LED lighting upgrades
• - Security Lighting
• - Switchboard upgrades
• - Test and Tag
• - Commercial Property
• - General Electrical Maintenance

```html
<!DOCTYPE html>
<html lang="en">
<head>
<meta charset="utf-8">
<title>Torvin Electrics – A5 Flyer</title>
<link href="https://fonts.googleapis.com/css2?family=Open+Sans:wght@400;600;700;800&display=swap" rel="stylesheet">
<style>
  :root {
    --blue: #0292cd;
    --blue-mid: #33a6d7;
    --blue-light: #85cae6;
    --blue-deep: #3176b5;
    --ink: #333333;
    --ink-dark: #1b1b1b;
    --white: #ffffff;
    --grey: #5c5c5c;
    --grey-dark: #474747;
    --stage: #dcdcdc;
  }
  html, body {
    margin: 0;
    padding: 0;
    width: 880px;
    height: 1200px;
    overflow: hidden;
    background: var(--stage);
    font-family: "Open Sans", Arial, sans-serif;
  }
  .canvas {
    position: relative;
    width: 880px;
    height: 1200px;
  }
  .flyer-side {
    position: absolute;
    top: 308px;
    width: 412px;
    height: 583px;
    box-shadow: 0 6px 18px rgba(0,0,0,0.25);
    background: var(--white);
  }
  .flyer-front { left: 18px; }
  .flyer-back { left: 450px; }
  .flyer-side svg { display: block; width: 100%; height: 100%; }
  .brand-name { font-weight: 700; fill: var(--ink); }
  .tagline { font-weight: 700; font-size: 10px; fill: var(--ink-dark); }
  .headline { font-weight: 700; font-size: 16.5px; fill: var(--blue); }
  .offer-big { font-weight: 800; fill: var(--ink-dark); }
  .offer-small { font-weight: 600; font-size: 9.5px; fill: var(--ink-dark); }
  .contact-title { font-weight: 700; font-size: 14px; fill: var(--white); }
  .contact-line { font-size: 11px; fill: var(--white); }
  .terms { font-size: 9px; fill: var(--ink-dark); }
  .services-title { font-weight: 700; font-size: 12.5px; fill: var(--ink-dark); }
  .service-item { font-size: 12.5px; fill: var(--white); }
  .back-detail { font-size: 11px; fill: var(--ink-dark); font-weight: 600; }
</style>
</head>
<body>
<div class="canvas">

  <!-- FRONT SIDE -->
  <div class="flyer-side flyer-front">
    <svg viewBox="0 0 426 602" xmlns="http://www.w3.org/2000/svg">
      <defs>
        <linearGradient id="paper" x1="0" y1="0" x2="1" y2="1">
          <stop offset="0" stop-color="#ffffff"/>
          <stop offset="0.6" stop-color="#eeeeee"/>
          <stop offset="1" stop-color="#dcdcdc"/>
        </linearGradient>
        <linearGradient id="photoInterior" x1="0" y1="0" x2="0" y2="1">
          <stop offset="0" stop-color="#f2f0ec"/>
          <stop offset="0.6" stop-color="#d9cfc4"/>
          <stop offset="1" stop-color="#bfb4a8"/>
        </linearGradient>
        <linearGradient id="photoHouse" x1="0" y1="0" x2="1" y2="1">
          <stop offset="0" stop-color="#5e6a55"/>
          <stop offset="0.5" stop-color="#8a8f78"/>
          <stop offset="1" stop-color="#3f7f99"/>
        </linearGradient>
        <linearGradient id="photoExterior" x1="0" y1="0" x2="1" y2="1">
          <stop offset="0" stop-color="#2f3a48"/>
          <stop offset="0.5" stop-color="#c9a76a"/>
          <stop offset="1" stop-color="#e8e2d8"/>
        </linearGradient>
        <linearGradient id="blueSweep" x1="0" y1="0" x2="1" y2="1">
          <stop offset="0" stop-color="var(--blue-mid)"/>
          <stop offset="1" stop-color="var(--blue)"/>
        </linearGradient>
        <radialGradient id="sticker" cx="0.4" cy="0.35" r="0.7">
          <stop offset="0" stop-color="#f4f4f4"/>
          <stop offset="1" stop-color="#bdbdbd"/>
        </radialGradient>
      </defs>

      <rect class="paper" width="426" height="602" fill="url(#paper)"/>

      <!-- photos -->
      <path d="M282 0 L426 0 L426 220 L252 220 C 262 140 272 70 282 0 Z" fill="url(#photoInterior)" role="img" aria-label="Photo: bright modern kitchen and dining interior with pendant lights"/>
      <path d="M246 226 L426 226 L426 378 L222 378 C 230 320 238 270 246 226 Z" fill="url(#photoHouse)" role="img" aria-label="Photo: new two-storey home with garden and pool at dusk"/>
      <rect x="0" y="392" width="300" height="184" fill="url(#photoExterior)" role="img" aria-label="Photo: renovated weatherboard house with lit verandah at dusk"/>

      <!-- left curve accents -->
      <path d="M292 0 C 278 110 262 210 232 290 C 210 350 180 380 120 392" fill="none" stroke="var(--grey-dark)" stroke-width="7"/>
      <path d="M300 0 C 286 110 270 210 240 290" fill="none" stroke="var(--blue-mid)" stroke-width="3"/>

      <!-- bottom white strip -->
      <rect x="0" y="576" width="426" height="26" fill="var(--white)"/>

      <!-- blue contact sweep -->
      <path d="M160 602 C 230 470 320 385 426 352 L426 368 C 330 400 240 480 178 602 Z" fill="var(--grey-dark)"/>
      <path d="M178 602 C 240 480 330 400 426 368 L426 602 Z" fill="url(#blueSweep)"/>

      <!-- logo -->
      <circle cx="48" cy="56" r="24" fill="var(--blue)"/>
      <text class="brand-name" x="80" y="64" font-size="20">Torvin Electrics</text>
      <text class="tagline" x="22" y="109">Residential - Commercial - Industrial</text>

      <!-- headline -->
      <text class="headline" x="22" y="158">SPECIALISING In</text>
      <text class="headline" x="22" y="178">New Homes,</text>
      <text class="headline" x="22" y="198">Renovations And</text>
      <text class="headline" x="22" y="218">Commercial Projects</text>

      <!-- offers -->
      <circle cx="182" cy="306" r="62" fill="var(--white)" opacity="0.8"/>
      <circle cx="182" cy="306" r="56" fill="url(#sticker)"/>
      <text class="offer-big" x="138" y="305" font-size="26">10%</text>
      <text class="offer-big" x="195" y="322" font-size="16">off</text>
      <text class="offer-small" x="182" y="340" text-anchor="middle">all electrical</text>
      <text class="offer-small" x="182" y="352" text-anchor="middle">services *</text>

      <circle cx="78" cy="390" r="66" fill="var(--white)" opacity="0.85"/>
      <circle cx="78" cy="390" r="60" fill="url(#sticker)"/>
      <text class="offer-big" x="76" y="389" font-size="26" text-anchor="middle">FREE</text>
      <text class="offer-small" x="76" y="405" text-anchor="middle">LED downlights</text>
      <text class="offer-small" x="76" y="418" text-anchor="middle">on installation *</text>

      <!-- contact -->
      <text class="contact-title" x="408" y="465" text-anchor="end">Contact details</text>
      <line x1="330" y1="473" x2="408" y2="473" stroke="var(--white)" stroke-width="1.5"/>
      <!-- phone icon -->
      <path d="M328 498 h8 v2 h-2 v3 h-4 v-3 h-2 Z" fill="var(--white)"/>
      <text class="contact-line" x="408" y="505" text-anchor="end">0457 613 948</text>
      <!-- mail icon -->
      <rect x="247" y="517" width="9" height="6" fill="var(--white)"/>
      <path d="M247 517 L251.5 521 L256 517" fill="none" stroke="var(--blue)" stroke-width="1"/>
      <text class="contact-line" x="408" y="524" text-anchor="end">admin@torvinelectrics.com.au</text>
      <rect x="322" y="537" width="9" height="9" fill="var(--white)"/>
      <text class="contact-line" x="408" y="546" text-anchor="end">/TorvinElectrics</text>
      <text class="contact-line" x="408" y="570" text-anchor="end">Lic no. 51327</text>
      <text class="contact-line" x="408" y="585" text-anchor="end">ABN 48 719 205 316</text>

      <text class="terms" x="34" y="593">*Terms conditions apply</text>
    </svg>
  </div>

  <!-- BACK SIDE -->
  <div class="flyer-side flyer-back">
    <svg viewBox="0 0 426 602" xmlns="http://www.w3.org/2000/svg">
      <defs>
        <linearGradient id="paperBack" x1="0" y1="0" x2="1" y2="1">
          <stop offset="0" stop-color="#ffffff"/>
          <stop offset="1" stop-color="#dedede"/>
        </linearGradient>
        <linearGradient id="photoPool" x1="0" y1="0" x2="0" y2="1">
          <stop offset="0" stop-color="#e9ebe8"/>
          <stop offset="0.55" stop-color="#8a7a62"/>
          <stop offset="0.8" stop-color="#2f8fb0"/>
          <stop offset="1" stop-color="#4a3222"/>
        </linearGradient>
        <linearGradient id="photoLounge" x1="0" y1="0" x2="0" y2="1">
          <stop offset="0" stop-color="#2a2a2e"/>
          <stop offset="0.5" stop-color="#8b7a66"/>
          <stop offset="1" stop-color="#3a2b22"/>
        </linearGradient>
        <linearGradient id="photoKitchen" x1="0" y1="0" x2="0" y2="1">
          <stop offset="0" stop-color="#f1f1f1"/>
          <stop offset="0.5" stop-color="#5a4a40"/>
          <stop offset="1" stop-color="#d8d8d8"/>
        </linearGradient>
        <linearGradient id="blueBack" x1="0" y1="0" x2="1" y2="1">
          <stop offset="0" stop-color="var(--blue-mid)"/>
          <stop offset="1" stop-color="var(--blue)"/>
        </linearGradient>
        <linearGradient id="banner" x1="0" y1="0" x2="1" y2="0">
          <stop offset="0" stop-color="#ffffff" stop-opacity="0"/>
          <stop offset="0.3" stop-color="#e6e6e6"/>
          <stop offset="1" stop-color="#d2d2d2"/>
        </linearGradient>
      </defs>

      <rect width="426" height="602" fill="url(#paperBack)"/>

      <!-- photos -->
      <rect x="0" y="0" width="426" height="160" fill="url(#photoPool)" role="img" aria-label="Photo: modern house with illuminated pool deck at dusk"/>
      <rect x="0" y="166" width="230" height="164" fill="url(#photoLounge)" role="img" aria-label="Photo: outdoor lounge with wall-mounted downlights at night"/>
      <rect x="0" y="336" width="170" height="266" fill="url(#photoKitchen)" role="img" aria-label="Photo: kitchen with pendant lights over a bench"/>

      <!-- blue services panel -->
      <path d="M426 88 C 330 128 240 190 190 262 C 110 372 60 480 34 602 L426 602 Z" fill="var(--grey-dark)"/>
      <path d="M426 98 C 334 136 248 196 200 266 C 122 374 72 482 46 602 L426 602 Z" fill="url(#blueBack)"/>

      <!-- grey corner panel -->
      <path d="M426 298 C 360 368 310 478 292 602 L426 602 Z" fill="var(--grey-dark)"/>
      <path d="M426 306 C 366 376 318 484 302 602 L426 602 Z" fill="#ececec"/>

      <!-- banner -->
      <rect x="118" y="196" width="308" height="36" fill="url(#banner)"/>
      <text class="services-title" x="298" y="212" text-anchor="middle">ALL RESIDENTIAL &amp; COMMERCIAL</text>
      <text class="services-title" x="298" y="226" text-anchor="middle">ELECTRICAL SERVICES</text>

      <!-- service list -->
      <g class="service-list">
        <text class="service-item" x="215" y="260">✓ New Home installations</text>
        <text class="service-item" x="197" y="282">✓ Commercial projects</text>
        <text class="service-item" x="180" y="304">✓ Shop fit outs</text>
        <text class="service-item" x="163" y="326">✓ Renovations</text>
        <text class="service-item" x="146" y="348">✓ Smoke Detectors</text>
        <text class="service-item" x="133" y="370">✓ Air Conditioning and Ceiling Fans</text>
        <text class="service-item" x="121" y="392">✓ Garden Lighting</text>
        <text class="service-item" x="110" y="414">✓ Oven and Cooktop Installations</text>
        <text class="service-item" x="99" y="436">✓ Power Point installation</text>
        <text class="service-item" x="90" y="458">✓ LED lighting upgrades</text>
        <text class="service-item" x="80" y="482">✓ Security Lighting</text>
        <text class="service-item" x="71" y="504">✓ Switchboard upgrades</text>
        <text class="service-item" x="63" y="526">✓ Test and Tag</text>
        <text class="service-item" x="57" y="548">✓ Commercial Property</text>
        <text class="service-item" x="50" y="570">✓ General Electrical Maintenance</text>
      </g>

      <!-- right details -->
      <rect x="364" y="444" width="18" height="18" rx="3" fill="var(--blue-deep)"/>
      <text class="back-detail" x="408" y="480" text-anchor="end">/TorvinElectrics</text>
      <circle cx="330" cy="530" r="19" fill="var(--blue)"/>
      <text class="brand-name" x="354" y="535" font-size="11">Torvin</text>
      <text class="brand-name" x="354" y="547" font-size="8">Electrics</text>
      <text class="back-detail" x="312" y="573">Lic no. 51327</text>
      <text class="back-detail" x="312" y="587">ABN 48 719 205 316</text>
    </svg>
  </div>

</div>
</body>
</html>
```